Business Cards for new orthopaedic surgery practice

My husband and I are starting our own orthopaedic surgery practice. We are looking for a business card that is uniform, but one will have my name/title and the other will have his. You can just create one design with my name on it for now. But when I choose your design as the winning design I will ask that you add another copy with his name/title.

We are looking for classy, simple, elite all in one. We like dark blues/a little gold/yellow. Something that goes with our logo. We want our logo incorporated. Here is all the info you need:
Business name: RV Spine & Vitality Center
Location: 38157 North Harbor Blvd
Coral Springs, FL 33058
Phone: 954-218-4630
Fax: 954-581-2473
Email: info@myrvspine.example

Names: Lorena Vickers, M.D.
Board Certified Hand and Upper Extremity Surgeon

Eban Sorley, M.D.
Board Certified Hip & Knee Replacement/General Orthopaedic Surgeon

Can decide what you want to put on the back. Maybe a slogan:
Rooted in Care. Focused on You

I am just going to upload our logo. The only thing is if we select you as the winning design, the location, and phone numbers may change. We will need your help to update that once fully solidified.

Industry/Entity Type

Medical

Contact Information for Business Card

Colors
0054AA
0677BA
7BADD7
CADEEF
E8F1F8
0094D4
00A9DD
6FCCEA
C7EBF8
E9F6FB

Requirements
Must have
• class, appeal,
Should not have
• We want to air on the side of masculine if we are looking at masculine vs. feminine feel. But we still want it classy, sophisticated, and something we will love

```html
<!DOCTYPE html>
<html lang="en">
<head>
<meta charset="utf-8">
<title>RV Spine &amp; Vitality Center – Business Cards</title>
<link href="https://fonts.googleapis.com/css2?family=Montserrat:wght@400;500;600;700&display=swap" rel="stylesheet">
<style>
  :root {
    --navy: #1b2a52;
    --navy-deep: #16234a;
    --navy-soft: #23366a;
    --gold: #c9a15a;
    --white: #ffffff;
    --stage: #5e5e5e;
  }
  * { box-sizing: border-box; margin: 0; padding: 0; }
  html, body { width: 1200px; height: 875px; overflow: hidden; }
  body {
    background: var(--stage);
    font-family: "Montserrat", Arial, sans-serif;
    display: flex;
    align-items: center;
    justify-content: center;
    gap: 36px;
  }
  .card {
    position: relative;
    width: 546px;
    height: 312px;
    background: var(--navy);
    border-radius: 18px;
    overflow: hidden;
    box-shadow: 0 14px 30px rgba(0,0,0,.35);
  }

  /* Back side */
  .card-back .brand-mark {
    position: absolute;
    left: 50%;
    top: 44%;
    transform: translate(-50%, -50%);
    display: flex;
    flex-direction: column;
    align-items: center;
    gap: 12px;
  }
  .card-back .brand-circle {
    width: 78px; height: 78px;
    border-radius: 50%;
    border: 2px solid var(--navy-soft);
  }
  .card-back .brand-name {
    font-weight: 600;
    font-size: 15px;
    letter-spacing: 2px;
    text-transform: uppercase;
    color: var(--navy-soft);
  }
  .card-back .slogan {
    position: absolute;
    left: 0; right: 0;
    bottom: 52px;
    text-align: center;
    color: var(--gold);
    font-weight: 600;
    font-size: 17px;
    letter-spacing: .3px;
  }

  /* Front side */
  .card-front .gold-band {
    position: absolute;
    left: 0; right: 0; bottom: 0;
    height: 12px;
    background: var(--gold);
  }
  .card-front .brand-mark {
    position: absolute;
    left: 34px;
    top: 50%;
    transform: translateY(-56%);
    width: 200px;
    display: flex;
    flex-direction: column;
    align-items: center;
    gap: 12px;
    text-align: center;
  }
  .card-front .brand-circle {
    width: 70px; height: 70px;
    border-radius: 50%;
    border: 2px solid var(--gold);
  }
  .card-front .brand-name {
    color: var(--white);
    font-weight: 600;
    font-size: 14px;
    letter-spacing: 1.6px;
    line-height: 1.5;
    text-transform: uppercase;
  }
  .card-front .divider {
    position: absolute;
    left: 258px;
    top: 62px;
    width: 1.5px;
    height: 160px;
    background: var(--gold);
  }
  .card-front .details {
    position: absolute;
    left: 280px;
    top: 58px;
    color: var(--white);
    font-size: 11.5px;
    line-height: 1.38;
  }
  .details .doctor-name {
    color: var(--gold);
    font-weight: 700;
    font-size: 17px;
    line-height: 1.2;
  }
  .details .doctor-title { margin-bottom: 12px; }
  .details .address { margin-bottom: 10px; }
  .details .contact-line {
    display: flex;
    align-items: center;
    gap: 7px;
  }
  .details .contact-line svg { width: 10px; height: 10px; fill: var(--gold); flex: none; }
</style>
</head>
<body>

  <section class="card card-back" aria-label="Card back">
    <div class="brand-mark">
      <span class="brand-circle"></span>
      <span class="brand-name">RV Spine &amp; Vitality Center</span>
    </div>
    <p class="slogan">Rooted in Care. Focused on You</p>
  </section>

  <section class="card card-front" aria-label="Card front">
    <div class="brand-mark">
      <span class="brand-circle"></span>
      <span class="brand-name">RV Spine &amp;<br>Vitality Center</span>
    </div>
    <span class="divider"></span>
    <div class="details">
      <p class="doctor-name">Lorena Vickers, M.D.</p>
      <p class="doctor-title">Board Certified Hand and<br>Upper Extremity Surgeon</p>
      <p class="address">38157 North Harbor Blvd<br>Coral Springs, FL 33058</p>
      <p class="contact-line">
        <svg viewBox="0 0 24 24" aria-hidden="true"><path d="M6.6 10.8a15 15 0 0 0 6.6 6.6l2.2-2.2a1 1 0 0 1 1-.25 11.4 11.4 0 0 0 3.6.57 1 1 0 0 1 1 1V20a1 1 0 0 1-1 1A17 17 0 0 1 3 4a1 1 0 0 1 1-1h3.5a1 1 0 0 1 1 1c0 1.25.2 2.45.57 3.57a1 1 0 0 1-.25 1z"/></svg>
        954-218-4630
      </p>
      <p class="contact-line">
        <svg viewBox="0 0 24 24" aria-hidden="true"><path d="M6 2h10l2 2v4H6zM3 9h18a1 1 0 0 1 1 1v8h-4v4H6v-4H2v-8a1 1 0 0 1 1-1zm5 8v3h8v-3z"/></svg>
        954-581-2473
      </p>
      <p class="contact-line">
        <svg viewBox="0 0 24 24" aria-hidden="true"><path d="M2 5h20v14H2zm2 2v.5l8 5 8-5V7z"/></svg>
        info@myrvspine.example
      </p>
    </div>
    <span class="gold-band"></span>
  </section>

</body>
</html>
```